Business Card Design for Photographer

Updating business card design. Must use included logo. We're a luxury wedding photography business. Elegancy, luxury, consistency are messages we wish to convey.

Visit our website at www.colbyvarnway.com to familiarize yourself more with our brand design currently (fonts, colors etc.). This is what we want to maintain.

Target Market(s)

Luxury Brides and Grooms

Industry/Entity Type

Wedding

Contact Information for Business Card

Current logo (attached to brief)
Name: Colby Varnway
Phone: 5208813047
website/blog
Email

Requirements
Must have
• Current logo (attached to brief)
• Name: Colby Varnway
• Phone: 5208813047
• website/blog
• Email
• Instagram username
Should not have
• bright colors, fonts that don't suit our brand (visit www.colbyvarnway.com)

```html
<!DOCTYPE html>
<html lang="en">
<head>
<meta charset="utf-8">
<title>Colby Varnway Photographers – Business Card</title>
<link rel="stylesheet" href="https://fonts.googleapis.com/css2?family=Tenor+Sans&family=Source+Sans+3:wght@400&display=swap">
<style>
  :root {
    --page: #f4f4f4;
    --navy: #2a2058;
    --plum: #8e2a7e;
    --rose: #e2b4cb;
    --sky: #4a9fd2;
    --lilac: #dcd0e4;
    --white: #ffffff;
    --grey: #767676;
    --magenta: #d0288e;
  }
  html, body {
    margin: 0;
    width: 1200px;
    height: 387px;
    overflow: hidden;
    background: var(--page);
  }
  .sheet { position: relative; width: 1200px; height: 387px; }
  .card {
    position: absolute;
    top: 26px;
    width: 513px;
    height: 333px;
    background: var(--navy);
    overflow: hidden;
  }
  .card--front { left: 23px; }
  .card--back { left: 663px; }

  .card__artwork { position: absolute; }
  .card--front .card__artwork {
    inset: 0;
    background: radial-gradient(ellipse 62% 66% at 52% 50%,
      var(--white) 0%, var(--white) 52%, var(--lilac) 68%,
      var(--rose) 78%, var(--plum) 90%, var(--navy) 100%);
  }
  .card--back .card__artwork {
    right: 0; top: 0;
    width: 280px; height: 333px;
    background: radial-gradient(ellipse 75% 70% at 82% 22%,
      var(--white) 0%, var(--white) 30%, var(--rose) 55%,
      var(--plum) 80%, rgba(42, 32, 88, 0) 100%);
  }

  .brand {
    position: absolute;
    left: 0; right: 0;
    top: 112px;
    text-align: center;
    color: var(--grey);
    font-family: "Tenor Sans", sans-serif;
  }
  .brand__mark {
    display: block;
    width: 49px; height: 49px;
    margin: 0 auto 18px;
    background: var(--grey);
  }
  .brand__name {
    margin: 0;
    font-size: 23px;
    font-weight: 400;
    letter-spacing: 4px;
    text-transform: uppercase;
    line-height: 1;
  }
  .brand__trade {
    margin: 11px 0 0;
    font-size: 12px;
    letter-spacing: 4.5px;
    text-transform: uppercase;
    line-height: 1;
  }

  .nameplate {
    position: absolute;
    left: 0; top: 134px;
    width: 295px; height: 42px;
    background: var(--white);
    border-radius: 0 21px 21px 0;
    display: flex; align-items: center;
  }
  .nameplate__name {
    margin: 0 0 0 36px;
    font-family: "Tenor Sans", sans-serif;
    font-weight: 400;
    font-size: 29px;
    font-variant: small-caps;
    letter-spacing: 2px;
    color: var(--grey);
    line-height: 1;
  }
  .contact {
    position: absolute;
    left: 55px; top: 184px;
    margin: 0; padding: 0;
    list-style: none;
    font-family: "Source Sans 3", sans-serif;
    font-size: 15px;
    color: var(--magenta);
  }
  .contact__item {
    display: flex; align-items: center;
    height: 21px;
  }
  .contact__icon {
    width: 14px; height: 14px;
    margin-right: 9px;
    fill: var(--white);
    stroke: var(--white);
    flex: none;
  }
</style>
</head>
<body>
<div class="sheet">

  <section class="card card--front">
    <div class="card__artwork" role="img" aria-label="Decorative background artwork in white, lilac, rose and plum tones"></div>
    <div class="brand">
      <span class="brand__mark"></span>
      <h1 class="brand__name">Colby Varnway</h1>
      <p class="brand__trade">Photographers</p>
    </div>
  </section>

  <section class="card card--back">
    <div class="card__artwork" role="img" aria-label="Decorative corner artwork in white, rose and plum tones"></div>

    <div class="nameplate">
      <h2 class="nameplate__name">Colby Varnway</h2>
    </div>

    <ul class="contact">
      <li class="contact__item">
        <svg class="contact__icon" viewBox="0 0 16 16" aria-hidden="true"><path stroke="none" d="M4 1l3 3-2 2c1 2 3 4 5 5l2-2 3 3-2 3C7 15 1 9 1 3z"/></svg>
        (520) 881-3047
      </li>
      <li class="contact__item">
        <svg class="contact__icon" viewBox="0 0 16 16" aria-hidden="true"><rect x="1" y="3" width="14" height="10" stroke="none"/><path d="M1.5 3.5L8 9l6.5-5.5" fill="none" stroke="var(--navy)" stroke-width="1.3"/></svg>
        colby@colbyvarnway.com
      </li>
      <li class="contact__item">
        <svg class="contact__icon" viewBox="0 0 16 16" aria-hidden="true"><g fill="none" stroke-width="1.4"><circle cx="8" cy="8" r="6.5"/><ellipse cx="8" cy="8" rx="3" ry="6.5"/><path d="M1.5 8h13"/></g></svg>
        www.colbyvarnway.com
      </li>
      <li class="contact__item">
        <svg class="contact__icon" viewBox="0 0 16 16" aria-hidden="true"><rect x="2" y="2" width="12" height="12" stroke="none"/></svg>
        colbyvarnwayphoto
      </li>
    </ul>
  </section>

</div>
</body>
</html>
```